Meadowbrook Holdings Website Design

We have been redeveloping our website already and are quite happy with the content, but the design needs to be better:
https://trelvan-site.examplehost.net/

Pages, content, concept etc. Can all be taken from the redeveloped website.
The farmer can register and edit/view their profile, subscribe and these pages need to be designed better as well as contact, about, pricing, tos, privacy and a page with example portlets.

We need a website to appeal to farmers, investors and retiring farmers.

The design should be clean and a little country.

We don't want any repeat designs that some may submit to every project and has no respect for the project brief, so please don't submit them.

Target Market(s)

farmers, investors, retirees

Industry/Entity Type

Farming

Number of Pages Required

5+ page

Colors

Designer to choose colors to be used in the design.

Requirements
Must have
• Nice, clean modern design that is appealing
• Profile page laid out nicely

```html
<!DOCTYPE html>
<html lang="en">
<head>
<meta charset="utf-8">
<title>Meadowbrook Holdings – You Can Own A Farm</title>
<link href="https://fonts.googleapis.com/css2?family=Courgette&family=Quicksand:wght@500;700&family=Arimo:wght@400;700&display=swap" rel="stylesheet">
<style>
:root{
  --green:#5c9e0f;
  --green-dark:#4d8a0a;
  --red:#e21d2a;
  --ink:#1a1a1a;
  --charcoal:#222222;
  --text:#444444;
  --muted:#777777;
  --light:#f2f2f2;
  --white:#ffffff;
  --footer:#3a3a3a;
}
*{box-sizing:border-box;margin:0;padding:0}
html,body{width:1200px;height:2871px;overflow:hidden}
body{position:relative;font-family:"Arimo",Arial,sans-serif;color:var(--text);background:var(--white)}
.abs{position:absolute}
a{color:inherit;text-decoration:none}

/* top bar */
.topbar{top:0;left:0;width:1200px;height:46px;background:var(--light)}
.topbar-accent{top:0;left:0;width:1200px;height:4px;background:linear-gradient(90deg,var(--red) 0 50%,var(--green) 50% 100%)}
.topbar-phone{top:16px;left:66px;font-size:14px;color:var(--text);display:flex;align-items:center;gap:8px}
.topbar-phone svg{width:18px;height:18px}
.social{display:flex;gap:10px}
.social span{width:28px;height:28px;border:1px solid #bbb;border-radius:50%;background:var(--white);display:block}
.topbar .social{position:absolute;top:10px;left:924px}
.login{top:4px;left:1005px;width:130px;height:42px;background:var(--green);color:var(--white);font:700 15px "Arimo",sans-serif;display:flex;align-items:center;justify-content:center;gap:8px;clip-path:polygon(14% 0,100% 0,100% 100%,0 100%)}

/* header */
.header{top:46px;left:0;width:1200px;height:84px;background:var(--white)}
.brand{top:18px;left:64px;display:flex;align-items:center;gap:14px;font:700 29px "Quicksand",sans-serif;color:var(--charcoal)}
.brand i{width:44px;height:44px;border-radius:50%;background:var(--green);display:block}
.nav{top:34px;left:546px;display:flex;font-size:14px;color:var(--charcoal)}
.nav a{display:block;padding:0 18px;height:50px;position:relative}
.nav a.active::after{content:"";position:absolute;left:12px;right:12px;bottom:0;height:4px;background:var(--red)}

/* hero */
.hero{top:130px;left:0;width:1200px;height:586px;background:linear-gradient(100deg,#3b3a35 0%,#5b4a3c 35%,#6a5a48 55%,#3d3e38 100%)}
.hero-shade{inset:0;background:rgba(0,0,0,.25)}
.hero-title{top:193px;left:0;width:1200px;text-align:center;font:56px "Courgette",cursive;color:var(--white)}
.hero-sub{top:262px;left:0;width:1200px;text-align:center;font:27px "Arimo",sans-serif;color:var(--white)}
.btn{background:var(--green);color:var(--white);border-radius:30px;font:700 17px "Arimo",sans-serif;display:flex;align-items:center;justify-content:center;gap:12px;letter-spacing:.3px}
.btn svg,.login svg,.ghost svg{width:20px;height:20px}
.hero-btn{top:329px;left:493px;width:180px;height:52px}
.dots{top:534px;left:557px;display:flex;gap:10px}
.dots span{width:14px;height:14px;border:2px solid var(--white);border-radius:50%}
.dots span.on{background:var(--red)}

/* own a farm */
.own{top:716px;left:0;width:1200px;height:719px;background:linear-gradient(180deg,#f7f7f5 0%,#eeeeea 100%)}
.section-title{width:1200px;left:0;text-align:center;font:700 38px "Quicksand",sans-serif;color:var(--ink)}
.own .section-title{top:36px}
.lead{top:101px;left:0;width:1200px;text-align:center;font-size:15px;line-height:21px;color:var(--text)}
.divider{left:470px;width:260px;height:20px}
.own .divider{top:160px}
.steps-circles{top:225px;left:0;width:1200px}
.circle-item{position:absolute;width:280px;text-align:center}
.circle-item .ring{width:200px;height:200px;margin:0 auto;border:4px solid var(--green);border-radius:50%;background:var(--white);display:flex;align-items:center;justify-content:center}
.circle-item .ring div{width:100px;height:90px;border-radius:14px;background:#4a4a4a}
.circle-item p{margin-top:26px;font:700 19px/21px "Arimo",sans-serif;color:var(--ink)}
.circle-item svg{margin-top:16px;width:22px;height:22px}
.signup{top:578px;left:453px;width:295px;height:52px;font-size:19px}
.own-note{top:654px;left:0;width:1200px;text-align:center;font-size:15px;color:var(--text);text-decoration:underline}

/* process band */
.band{top:1435px;left:0;width:1200px;height:404px}
.band svg.bg{position:absolute;inset:0}
.step{position:absolute;top:0;width:400px;height:404px;color:var(--white)}
.step .num{position:absolute;top:-6px;font:500 150px/1 "Quicksand",sans-serif;opacity:.18;color:#fff}
.step h3{position:absolute;top:36px;font:400 25px/33px "Courgette",cursive;width:300px}
.step .rule{position:absolute;top:124px;width:190px;height:20px}
.step .glyph{position:absolute;top:170px;width:130px;height:120px;border-radius:14px;background:rgba(255,255,255,.92)}
.ghost{position:absolute;top:330px;width:142px;height:42px;border:2px solid var(--white);border-radius:22px;font-size:16px;color:var(--white);display:flex;align-items:center;justify-content:center;gap:8px}
.step-1 .num{left:34px;color:#555;opacity:.6}
.step-1 h3{left:130px}.step-1 .rule{left:112px}.step-1 .glyph{left:160px}.step-1 .ghost{left:153px}
.step-2{left:380px}
.step-2 .num{left:18px}.step-2 h3{left:70px;width:330px}.step-2 .rule{left:100px}.step-2 .glyph{left:128px}.step-2 .ghost{left:150px}
.step-3{left:800px}
.step-3 .num{left:34px}.step-3 h3{left:90px}.step-3 .rule{left:98px}.step-3 .glyph{left:110px}.step-3 .ghost{left:102px}

/* testimonials */
.testimonials{top:1839px;left:0;width:1200px;height:458px;background:var(--light)}
.testimonials .section-title{top:44px}
.testimonials .divider{top:111px}
.quote-card{top:186px;left:75px;width:1037px;height:134px;background:var(--white);box-shadow:0 2px 6px rgba(0,0,0,.08)}
.quote-card::after{content:"";position:absolute;left:52px;bottom:-16px;border:16px solid transparent;border-top-color:var(--white);border-bottom:0}
.avatar{top:32px;left:40px;width:70px;height:70px;border-radius:50%;background:linear-gradient(160deg,#c79a80,#7b4b38)}
.quote-text{top:32px;left:133px;width:860px;font-size:12px;line-height:22px;color:var(--muted)}
.quote-corner{right:0;bottom:0;width:48px;height:48px}
.author{top:363px;left:86px;font:13px "Georgia",serif;color:var(--ink)}
.author small{display:block;font-size:11px;color:var(--muted);margin-top:6px}
.t-dots{top:379px;left:1022px;display:flex;gap:7px}
.t-dots span{width:8px;height:8px;border-radius:50%;background:#ddd}
.t-dots span.on{background:var(--green)}

/* produce strip */
.produce{top:2297px;left:0;width:1200px;height:143px;background:linear-gradient(90deg,#8a3a1c 0%,#e0a820 12%,#f0c830 22%,#d83a2a 34%,#7a1f3a 48%,#d83a2a 60%,#f0c830 74%,#9cc040 86%,#8a3a1c 100%)}

/* newsletter */
.subscribe-title{top:2486px;left:77px;font:700 24px "Quicksand",sans-serif;color:var(--ink)}
.email{top:2475px;left:354px;width:520px;height:54px;border:1px solid #ddd;border-radius:6px;padding:0 14px;font-size:14px;color:#999;display:flex;align-items:center}
.subscribe-btn{top:2475px;left:902px;width:225px;height:54px;font-size:16px;border-radius:28px}

/* footer links */
.footer-col{top:2588px;font-size:14px;color:var(--text)}
.footer-col h4{font:700 17px "Arimo",sans-serif;color:var(--green);letter-spacing:.5px;margin-bottom:14px}
.footer-col li{list-style:none;line-height:32px;display:flex;gap:8px;align-items:center}
.footer-col li::before{content:"»";color:var(--green);font-weight:700}
.footer-col address{font-style:normal;line-height:21px}
.footer-col .mail{display:block;margin-top:12px;text-decoration:underline}
.footer-col .social{margin-top:24px}
.col-products{left:77px}.col-learn{left:237px}.col-about{left:504px}.col-contact{left:711px}.col-touch{left:926px}
.bottom-bar{top:2814px;left:0;width:1200px;height:57px;background:var(--footer);color:var(--white);font-size:14px;display:flex;align-items:center;justify-content:center}
</style>
</head>
<body>

<div class="abs topbar">
  <div class="abs topbar-phone">
    <svg viewBox="0 0 20 20"><circle cx="10" cy="10" r="9" fill="none" stroke="#666" stroke-width="1.5"/><path d="M7 5.5l1.8 2.2-1 1.2c.6 1.2 1.6 2.2 2.8 2.8l1.2-1 2.2 1.8-1 1.7C9.5 14.2 5.8 10.5 5.3 7z" fill="#666"/></svg>
    Speak to an account executive now 555-010-4821
  </div>
  <div class="social"><span></span><span></span></div>
</div>
<div class="abs topbar-accent"></div>
<a class="abs login" href="#">LOGIN <svg viewBox="0 0 20 20"><circle cx="10" cy="10" r="8.5" fill="none" stroke="#fff" stroke-width="1.8"/><path d="M6 10h7M10 6.5l3.5 3.5-3.5 3.5" fill="none" stroke="#fff" stroke-width="1.8"/></svg></a>

<header class="abs header">
  <div class="abs brand"><i></i>Meadowbrook Holdings</div>
  <nav class="abs nav">
    <a class="active" href="#">Home</a><a href="#">Aspiring Farmers</a><a href="#">Investors</a><a href="#">Retiring Farmer</a><a href="#">Blog</a><a href="#">Pricing</a>
  </nav>
</header>

<section class="abs hero">
  <div class="abs" role="img" aria-label="Photo of a farmer sitting outdoors with two young children and a dog" style="inset:0"></div>
  <div class="abs hero-shade"></div>
  <h1 class="abs hero-title">We Grow Best Food</h1>
  <p class="abs hero-sub">Helping young families own and run their own farm</p>
  <a class="abs btn hero-btn" href="#">READ MORE <svg viewBox="0 0 20 20"><circle cx="10" cy="10" r="8.5" fill="none" stroke="#fff" stroke-width="1.8"/><path d="M6 10h7M10 6.5l3.5 3.5-3.5 3.5" fill="none" stroke="#fff" stroke-width="1.8"/></svg></a>
  <div class="abs dots"><span></span><span class="on"></span><span></span><span></span></div>
</section>

<section class="abs own">
  <h2 class="abs section-title">You Can Own A Farm</h2>
  <p class="abs lead">We know how hard it is for a young family to find the capital required to own and operate their own farm - so we started Meadowbrook Holdings.<br>We want to rejuvenate regional Australia by putting farming back up the top of the career list for anyone.</p>
  <svg class="abs divider" viewBox="0 0 260 20"><line x1="0" y1="10" x2="110" y2="10" stroke="#5c9e0f"/><line x1="150" y1="10" x2="260" y2="10" stroke="#5c9e0f"/><circle cx="130" cy="10" r="7" fill="#5c9e0f"/></svg>
  <div class="abs steps-circles">
    <div class="circle-item" style="left:27px"><div class="ring"><div role="img" aria-label="Icon of a young family by a house"></div></div><p>We connect a young<br>farming family</p><svg viewBox="0 0 22 22"><circle cx="11" cy="11" r="9" fill="none" stroke="#222" stroke-width="1.6"/><path d="M7 11h7M11 7.5l3.5 3.5-3.5 3.5" fill="none" stroke="#222" stroke-width="1.6"/></svg></div>
    <div class="circle-item" style="left:314px"><div class="ring"><div role="img" aria-label="Icon of a retiring couple under an umbrella"></div></div><p>with a retiring<br>farming family</p><svg viewBox="0 0 22 22"><circle cx="11" cy="11" r="9" fill="none" stroke="#222" stroke-width="1.6"/><path d="M7 11h7M11 7.5l3.5 3.5-3.5 3.5" fill="none" stroke="#222" stroke-width="1.6"/></svg></div>
    <div class="circle-item" style="left:603px"><div class="ring"><div role="img" aria-label="Icon of investors around a coin"></div></div><p>and<br>investors</p><svg viewBox="0 0 22 22"><circle cx="11" cy="11" r="9" fill="none" stroke="#222" stroke-width="1.6"/><path d="M7 11h7M11 7.5l3.5 3.5-3.5 3.5" fill="none" stroke="#222" stroke-width="1.6"/></svg></div>
    <div class="circle-item" style="left:892px"><div class="ring"><div role="img" aria-label="Icon of a farmhouse"></div></div><p>to own and operate<br>a farm together</p><svg viewBox="0 0 22 22"><circle cx="11" cy="11" r="9" fill="none" stroke="#222" stroke-width="1.6"/><path d="M7 11h7M11 7.5l3.5 3.5-3.5 3.5" fill="none" stroke="#222" stroke-width="1.6"/></svg></div>
  </div>
  <a class="abs btn signup" href="#">SIGNING UP NOW <svg viewBox="0 0 20 20"><circle cx="10" cy="10" r="8.5" fill="none" stroke="#fff" stroke-width="1.8"/><path d="M6 10h7M10 6.5l3.5 3.5-3.5 3.5" fill="none" stroke="#fff" stroke-width="1.8"/></svg></a>
  <p class="abs own-note">you will help us get you farm-ready and to find your dream farm.</p>
</section>

<section class="abs band">
  <svg class="bg" viewBox="0 0 1200 404" preserveAspectRatio="none">
    <rect width="1200" height="404" fill="#5c9e0f"/>
    <polygon points="0,0 356,0 440,404 0,404" fill="#222222"/>
    <polygon points="842,0 1200,0 1200,404 762,404" fill="#e21d2a"/>
  </svg>
  <div class="step step-1">
    <span class="num">1</span>
    <h3>Register as an<br>Aspiring Farmer</h3>
    <svg class="rule" viewBox="0 0 190 20"><line x1="0" y1="10" x2="80" y2="10" stroke="#fff"/><line x1="110" y1="10" x2="190" y2="10" stroke="#fff"/><circle cx="95" cy="10" r="6" fill="#fff"/></svg>
    <div class="glyph" role="img" aria-label="Add user icon"></div>
    <a class="ghost" href="#">Register <svg viewBox="0 0 20 20"><circle cx="10" cy="10" r="8.5" fill="none" stroke="#fff" stroke-width="1.8"/><path d="M6 10h7M10 6.5l3.5 3.5-3.5 3.5" fill="none" stroke="#fff" stroke-width="1.8"/></svg></a>
  </div>
  <div class="step step-2">
    <span class="num">2</span>
    <h3>Build your farm skills to get<br>yourself farm-ready.</h3>
    <svg class="rule" viewBox="0 0 190 20"><line x1="0" y1="10" x2="80" y2="10" stroke="#fff"/><line x1="110" y1="10" x2="190" y2="10" stroke="#fff"/><circle cx="95" cy="10" r="6" fill="#fff"/></svg>
    <div class="glyph" role="img" aria-label="Tractor icon"></div>
    <a class="ghost" href="#">Farm Ready <svg viewBox="0 0 20 20"><circle cx="10" cy="10" r="8.5" fill="none" stroke="#fff" stroke-width="1.8"/><path d="M6 10h7M10 6.5l3.5 3.5-3.5 3.5" fill="none" stroke="#fff" stroke-width="1.8"/></svg></a>
  </div>
  <div class="step step-3">
    <span class="num">3</span>
    <h3>Together we find you<br>your dream farm.</h3>
    <svg class="rule" viewBox="0 0 190 20"><line x1="0" y1="10" x2="80" y2="10" stroke="#fff"/><line x1="110" y1="10" x2="190" y2="10" stroke="#fff"/><circle cx="95" cy="10" r="6" fill="#fff"/></svg>
    <div class="glyph" role="img" aria-label="Farmhouse icon"></div>
    <a class="ghost" href="#">Match Making <svg viewBox="0 0 20 20"><circle cx="10" cy="10" r="8.5" fill="none" stroke="#fff" stroke-width="1.8"/><path d="M6 10h7M10 6.5l3.5 3.5-3.5 3.5" fill="none" stroke="#fff" stroke-width="1.8"/></svg></a>
  </div>
</section>

<section class="abs testimonials">
  <h2 class="abs section-title">Our Testimonials</h2>
  <svg class="abs divider" viewBox="0 0 260 20"><line x1="0" y1="10" x2="110" y2="10" stroke="#5c9e0f"/><line x1="150" y1="10" x2="260" y2="10" stroke="#5c9e0f"/><circle cx="130" cy="10" r="7" fill="#5c9e0f"/></svg>
  <div class="abs quote-card">
    <div class="abs avatar" role="img" aria-label="Portrait photo of the reviewer"></div>
    <p class="abs quote-text">Joining was the best step our family has taken. The team matched us with a retiring couple who shared their land and their know-how, and our investors gave us the start we needed. We now run our own farm and feel part of a real community that truly cares about growing good food.</p>
    <svg class="abs quote-corner" viewBox="0 0 48 48"><polygon points="48,0 48,48 0,48" fill="#f07a1a"/><text x="30" y="40" font-family="Georgia,serif" font-size="20" fill="#fff">“</text></svg>
  </div>
  <p class="abs author">Mara Lindqvist<small>Home Owner, Newyork</small></p>
  <div class="abs t-dots"><span></span><span></span><span class="on"></span><span></span><span></span><span></span></div>
</section>

<div class="abs produce" role="img" aria-label="Row of fresh fruit: pineapples, bananas, melons, grapes, watermelon and berries"></div>

<h3 class="abs subscribe-title">Subscribe Newsletter</h3>
<div class="abs email">Enter Your Email</div>
<a class="abs btn subscribe-btn" href="#">SUBSCRIBE NOW <svg viewBox="0 0 20 20"><circle cx="10" cy="10" r="8.5" fill="none" stroke="#fff" stroke-width="1.8"/><path d="M6 10h7M10 6.5l3.5 3.5-3.5 3.5" fill="none" stroke="#fff" stroke-width="1.8"/></svg></a>

<div class="abs footer-col col-products"><h4>PRODUCTS</h4><ul><li>Tomatoes</li><li>Bell Peppers</li><li>Cucumbers</li><li>Ripe Reds</li><li>Valley Fresh</li></ul></div>
<div class="abs footer-col col-learn"><h4>LEARN</h4><ul><li>FreshPlate Kids™</li><li>In The Classroom</li><li>Future of Fresh</li><li>Greenhouse Education Center</li><li>Operation Think Fresh</li></ul></div>
<div class="abs footer-col col-about"><h4>ABOUT US</h4><ul><li>Innovation</li><li>The Grow-To People</li><li>Valley Fresh</li><li>The Bug Brigade</li><li>In the Community</li></ul></div>
<div class="abs footer-col col-contact"><h4>CONTACT</h4><ul><li>Contact Us</li><li>Careers</li><li>Blog</li><li>Calling All Bloggers</li><li>FAQs</li></ul></div>
<div class="abs footer-col col-touch"><h4>GET IN TOUCH</h4><address>12 Orchard Lane,<br>Millbrook, NY 641209<br>Canada</address><a class="mail" href="#">info@fieldlinefarms.example</a><div class="social"><span></span><span></span></div></div>

<footer class="abs bottom-bar">Fieldline Farms Learning Initiative. © 2017 Fieldline Farms . All rights reserved. Privacy Policy</footer>

</body>
</html>
```